Glumo Squish Orb (The RKQ stress reliever brought to you by Wumble)

Project Description: Glumo Squish Orb Box Design

Project Objective: Create a box design (H 2.842” x W 2.842” x D 2.842”) to hold a stress ball that combines humor and playfulness while emphasizing its stress-relief purpose. The design should subtly satirize the RKQ survey without being offensive. Think Dibbo Zing! Brand colors attached but it's not 100% necessary they are used. Design takes priority for this one.

Design Requirements and Guidance (Please only use suggestions. I want fresh, fun ideas!)

Text Ideas:
Stressed About RKQ? Squeeze for Serenity!
Solving RKQ Stress with Wumble, One Squeeze at a Time.
RKQ Made You Pull Your Hair Out? Squeeze This Instead!
Warning: Wumble May Cause Extreme CX Excellence.

Project Context: The Glumo Squish Orb is designed to humorously poke fun at our competitor, RKQ (Loyal Rating Tally), while serving as a practical stress-relief tool. It's intended for individuals familiar with RKQ and its challenges who can appreciate the humor behind using such a stress ball.

The goal is to add a playful and cheeky touch to the world of customer feedback metrics, making light of the sometimes-frustrating RKQ experience while providing genuine stress relief for users who may encounter RKQ-related stress.

Target Market(s)

Users of RKQ or similar customer satisfaction tool. CX professionals, Marketing Leaders.

Industry/Entity Type

Marketing Research, Tech

Font styles to use
Other font styles liked:
• Oxygen

Colors

Designer to choose colors to be used in the design.

Requirements
Must have
• Colorful, attention grabbing design, humorous text.

```html
<!DOCTYPE html>
<html lang="en">
<head>
<meta charset="utf-8">
<title>Glumo Squish Orb – Box Face</title>
<link rel="stylesheet" href="https://fonts.googleapis.com/css2?family=Fredoka:wght@600;700&family=Mali:wght@700&display=swap">
<style>
  :root {
    --stage: #eef1f4;
    --box-blue: #1fa3e6;
    --blob-white: #f6f7f8;
    --ink: #1c1f24;
    --lime: #e4f23a;
    --sun: #f3ee3e;
    --mint: #b9e64a;
    --tag-red: #e8261e;
    --white: #ffffff;
  }
  * { box-sizing: border-box; margin: 0; padding: 0; }
  html, body { width: 1200px; height: 900px; overflow: hidden; }
  body { background: var(--stage); position: relative; }

  .box-face {
    position: absolute;
    left: 230px; top: 80px;
    width: 740px; height: 740px;
    background: var(--box-blue);
    overflow: hidden;
    box-shadow: 0 10px 30px rgba(0,0,0,0.12);
  }
  .box-art { position: absolute; inset: 0; width: 100%; height: 100%; }

  .try-tag {
    position: absolute;
    left: 210px; top: 46px;
    width: 190px; height: 82px;
    background: var(--tag-red);
    border-radius: 12px;
    color: var(--white);
    font-family: "Fredoka", sans-serif;
    font-weight: 700;
    text-align: center;
    line-height: 1;
    padding-top: 8px;
  }
  .try-tag .try-word { display: block; font-size: 40px; }
  .try-tag .now-word { display: block; font-size: 26px; letter-spacing: 1px; }

  .headline {
    position: absolute;
    left: 0; right: 0; top: 300px;
    text-align: center;
    font-family: "Fredoka", sans-serif;
    font-weight: 700;
    color: var(--ink);
    line-height: 1.02;
    letter-spacing: 2px;
    text-transform: uppercase;
  }
  .headline .line-one { display: block; font-size: 66px; }
  .headline .line-two { display: block; font-size: 74px; }

  .tagline {
    position: absolute;
    left: 70px; top: 555px;
    font-family: "Mali", cursive;
    font-weight: 700;
    color: var(--lime);
    font-size: 58px;
    line-height: 1.05;
  }
  .tagline .line-one { display: block; padding-left: 70px; }
  .tagline .line-two { display: block; }
</style>
</head>
<body>
  <main class="box-face" aria-label="Glumo Squish Orb box front">
    <svg class="box-art" viewBox="0 0 740 740" aria-hidden="true">
      <!-- speed lines beside tag -->
      <g class="speed-lines" stroke="var(--tag-red)" stroke-width="8" stroke-linecap="round">
        <line x1="130" y1="62" x2="200" y2="62"/>
        <line x1="110" y1="84" x2="200" y2="84"/>
        <line x1="145" y1="106" x2="200" y2="106"/>
      </g>
      <g class="speed-dots" fill="var(--white)">
        <circle cx="96" cy="84" r="5"/><circle cx="118" cy="62" r="4"/><circle cx="132" cy="106" r="4"/>
      </g>
      <!-- arrow -->
      <path class="arrow" d="M420 150 Q470 165 480 225" fill="none" stroke="var(--white)" stroke-width="7" stroke-linecap="round"/>
      <path d="M458 210 L482 240 L500 205 Z" fill="var(--white)"/>
      <!-- blob -->
      <path class="blob" d="M250 250 C300 170 430 180 500 240 C580 300 600 420 520 470 C450 515 380 480 320 500 C250 520 200 470 215 400 C225 340 215 300 250 250 Z" fill="var(--blob-white)"/>
      <circle class="accent-sun" cx="370" cy="240" r="52" fill="var(--sun)" opacity="0.9"/>
      <circle class="accent-mint" cx="510" cy="455" r="58" fill="var(--mint)" opacity="0.9"/>
      <!-- sparkles -->
      <g class="sparkles" fill="var(--white)">
        <path d="M650 190 h8 v-10 h6 v10 h8 v6 h-8 v10 h-6 v-10 h-8 z"/>
        <path d="M90 560 h8 v-10 h6 v10 h8 v6 h-8 v10 h-6 v-10 h-8 z"/>
        <path d="M620 620 h8 v-10 h6 v10 h8 v6 h-8 v10 h-6 v-10 h-8 z"/>
      </g>
      <g class="confetti" fill="var(--tag-red)">
        <circle cx="610" cy="300" r="5"/><circle cx="150" cy="420" r="5"/><circle cx="690" cy="690" r="5"/>
      </g>
      <g class="dot-grid" fill="var(--white)" opacity="0.8">
        <circle cx="560" cy="650" r="3"/><circle cx="575" cy="650" r="3"/><circle cx="590" cy="650" r="3"/><circle cx="605" cy="650" r="3"/>
        <circle cx="560" cy="665" r="3"/><circle cx="575" cy="665" r="3"/><circle cx="590" cy="665" r="3"/><circle cx="605" cy="665" r="3"/>
        <circle cx="60" cy="300" r="3"/><circle cx="75" cy="300" r="3"/><circle cx="90" cy="300" r="3"/>
        <circle cx="60" cy="315" r="3"/><circle cx="75" cy="315" r="3"/><circle cx="90" cy="315" r="3"/>
      </g>
    </svg>

    <div class="try-tag"><span class="try-word">Try</span><span class="now-word">it NOW</span></div>

    <h1 class="headline"><span class="line-one">Stressed About</span><span class="line-two">RKQ ?</span></h1>

    <p class="tagline"><span class="line-one">Squeeze</span><span class="line-two">for Serenity!</span></p>
  </main>
</body>
</html>
```